Simple infographic for paper attributes

Hello, we are a company that sells paper. Any kind of paper, envelopes, letter paper, handicraft paper etc.

We need a graphic / infographic which indicates to our customers that our paper / envelopes etc. are both printable with printers and writable with any pens.

Font styles to use
Serif
Sans Serif

Requirements
Must have
• - The format would be 3000x3000 pixels.
- The style would be simple and simple
Nice to have
• - The two terms "printable" and "writable" may be used

```html
<!DOCTYPE html>
<html lang="en">
<head>
<meta charset="utf-8">
<title>Printable &amp; Writable</title>
<link rel="stylesheet" href="https://fonts.googleapis.com/css2?family=Bebas+Neue&family=Poppins:wght@500&display=swap">
<style>
  :root {
    --stage: #ececec;
    --frame-purple: #7f3f98;
    --tab-white: #ffffff;
    --heading-grey: #c9c9c9;
    --cyan: #0093d3;
    --magenta: #c8006a;
    --yellow: #f0c911;
    --black: #000000;
    --label-ink: #1f1f1f;
    --panel-light: #fbfbfb;
    --panel-shade: #e9e9e9;
  }
  html, body {
    margin: 0;
    width: 1056px;
    height: 1200px;
    overflow: hidden;
    background: var(--stage);
  }
  .infographic {
    position: absolute;
    left: 28px;
    top: 100px;
    width: 1000px;
    height: 1000px;
    display: block;
  }
  .heading {
    font-family: "Bebas Neue", "Oswald", sans-serif;
    font-size: 186px;
    fill: var(--heading-grey);
  }
  .step-number {
    font-family: "Bebas Neue", "Oswald", sans-serif;
    font-size: 236px;
    fill: #fff;
  }
  .use-label {
    font-family: "Poppins", "Helvetica Neue", Arial, sans-serif;
    font-weight: 500;
    font-size: 37px;
    fill: var(--label-ink);
  }
  .icon-line { fill: none; stroke: #fff; stroke-width: 6; stroke-linejoin: round; stroke-linecap: round; }
  .icon-fill { fill: #fff; }
</style>
</head>
<body>
<svg class="infographic" viewBox="66 59 1627 1627" xmlns="http://www.w3.org/2000/svg">
  <defs>
    <linearGradient id="panel-wash" x1="0" y1="0" x2="1" y2="1">
      <stop offset="0" stop-color="var(--panel-light)"/>
      <stop offset="0.5" stop-color="var(--panel-shade)"/>
      <stop offset="1" stop-color="var(--panel-light)"/>
    </linearGradient>
  </defs>

  <!-- frame -->
  <rect class="frame" x="66" y="59" width="1627" height="1627" fill="var(--frame-purple)"/>
  <path class="heading-tab" d="M103 59 H1655 V217 A85 85 0 0 1 1570 302 H188 A85 85 0 0 1 103 217 Z" fill="var(--tab-white)"/>
  <text class="heading" x="1380" y="256" text-anchor="middle" textLength="1415" lengthAdjust="spacingAndGlyphs" transform="translate(-500 0)">PRINTABLE &amp; WRITABLE</text>

  <!-- content panel -->
  <rect class="panel-backdrop" x="66" y="329" width="1627" height="1323" fill="url(#panel-wash)" role="img" aria-label="Soft white geometric hexagon backdrop"/>

  <!-- CMYK sheet -->
  <g class="cmyk-sheet">
    <path d="M330 401 H819 V699 H117 V616 H330 Z" fill="var(--cyan)"/>
    <path d="M117 606 L322 401 V606 Z" fill="var(--cyan)" stroke="#fff" stroke-width="7"/>
    <rect x="117" y="699" width="702" height="300" fill="var(--magenta)"/>
    <rect x="117" y="999" width="702" height="301" fill="var(--yellow)"/>
    <rect x="117" y="1300" width="702" height="303" fill="var(--black)"/>
  </g>

  <!-- connectors -->
  <g class="connectors">
    <rect x="940" y="541" width="701" height="17" fill="var(--cyan)"/>
    <rect x="940" y="840" width="701" height="17" fill="var(--magenta)"/>
    <rect x="940" y="1142" width="701" height="17" fill="var(--yellow)"/>
    <rect x="940" y="1441" width="701" height="17" fill="var(--black)"/>
  </g>

  <!-- step badges -->
  <g class="step-badges">
    <circle cx="819" cy="549" r="124" fill="#fff"/><circle cx="819" cy="549" r="101" fill="var(--cyan)"/>
    <text class="step-number" x="819" y="632" text-anchor="middle">1</text>
    <circle cx="819" cy="848" r="124" fill="#fff"/><circle cx="819" cy="848" r="101" fill="var(--magenta)"/>
    <text class="step-number" x="819" y="932" text-anchor="middle">2</text>
    <circle cx="819" cy="1150" r="124" fill="#fff"/><circle cx="819" cy="1150" r="101" fill="var(--yellow)"/>
    <text class="step-number" x="819" y="1233" text-anchor="middle">3</text>
    <circle cx="819" cy="1449" r="124" fill="#fff"/><circle cx="819" cy="1449" r="101" fill="var(--black)"/>
    <text class="step-number" x="819" y="1532" text-anchor="middle">4</text>
  </g>

  <!-- use icons -->
  <g class="use-icons">
    <!-- envelope -->
    <circle cx="1096" cy="549" r="100" fill="#fff"/><circle cx="1096" cy="549" r="83" fill="var(--cyan)"/>
    <rect class="icon-line" x="1044" y="519" width="104" height="64"/>
    <path class="icon-line" d="M1044 519 L1096 565 L1148 519 M1044 583 L1080 550 M1148 583 L1112 550"/>
    <!-- stack of paper -->
    <circle cx="1462" cy="549" r="100" fill="#fff"/><circle cx="1462" cy="549" r="83" fill="var(--cyan)"/>
    <path class="icon-line" d="M1450 504 H1500 L1462 574 H1414 Z"/>
    <path class="icon-line" d="M1505 514 L1468 584 H1420 M1509 525 L1473 594 H1424"/>
    <!-- letter in envelope -->
    <circle cx="1096" cy="848" r="100" fill="#fff"/><circle cx="1096" cy="848" r="83" fill="var(--magenta)"/>
    <path class="icon-line" d="M1066 835 V784 H1128 V835"/>
    <path class="icon-line" d="M1047 817 V884 H1146 V817 L1096 855 Z"/>
    <path class="icon-fill" d="M1089 777 L1096 770 L1103 777 Z"/>
    <!-- box -->
    <circle cx="1462" cy="848" r="100" fill="#fff"/><circle cx="1462" cy="848" r="83" fill="var(--magenta)"/>
    <path class="icon-line" d="M1407 816 L1462 784 L1518 816 L1462 848 Z M1407 816 V862 L1462 896 L1518 862 V816 M1462 848 V896"/>
    <path class="icon-line" d="M1434 800 L1490 832 M1414 842 L1450 862"/>
    <!-- tag -->
    <circle cx="1096" cy="1142" r="100" fill="#fff"/><circle cx="1096" cy="1142" r="83" fill="var(--yellow)"/>
    <path class="icon-fill" d="M1099 1090 H1148 V1140 L1091 1197 A8 8 0 0 1 1080 1197 L1041 1158 A8 8 0 0 1 1041 1147 Z"/>
    <circle cx="1126" cy="1112" r="8" fill="var(--yellow)"/>
    <!-- folder -->
    <circle cx="1462" cy="1142" r="100" fill="#fff"/><circle cx="1462" cy="1142" r="83" fill="var(--yellow)"/>
    <path class="icon-line" d="M1425 1113 H1484 L1490 1106 H1517 L1505 1185 H1418 L1403 1127 H1493 L1502 1163"/>
    <!-- roll and scissors -->
    <circle cx="1096" cy="1449" r="100" fill="#fff"/><circle cx="1096" cy="1449" r="83" fill="var(--black)"/>
    <ellipse class="icon-line" cx="1089" cy="1410" rx="20" ry="9"/>
    <path class="icon-line" d="M1069 1410 V1474 A20 9 0 0 0 1109 1474 V1410 M1069 1418 L1046 1436 L1058 1484 L1080 1480"/>
    <path class="icon-line" d="M1117 1442 L1138 1488 M1138 1442 L1117 1488"/>
    <circle class="icon-line" cx="1116" cy="1492" r="6"/><circle class="icon-line" cx="1139" cy="1492" r="6"/>
    <!-- business cards -->
    <circle cx="1465" cy="1449" r="100" fill="#fff"/><circle cx="1465" cy="1449" r="83" fill="var(--black)"/>
    <path class="icon-line" d="M1432 1416 L1452 1398 L1520 1442 M1466 1478 L1480 1500 L1498 1478"/>
    <rect x="1414" y="1420" width="102" height="56" fill="#fff"/>
    <circle cx="1430" cy="1434" r="7" fill="var(--black)"/>
    <rect x="1444" y="1442" width="60" height="5" fill="var(--black)"/>
    <rect x="1422" y="1454" width="82" height="5" fill="var(--black)"/>
    <rect x="1422" y="1465" width="82" height="5" fill="var(--black)"/>
  </g>

  <!-- labels -->
  <g class="use-labels">
    <text class="use-label" x="1096" y="676" text-anchor="middle">ENVELOPE</text>
    <text class="use-label" x="1466" y="676" text-anchor="middle">ANY KIND OF PAPER</text>
    <text class="use-label" x="1098" y="962" text-anchor="middle">LETTER PAPER</text>
    <text class="use-label" x="1466" y="962" text-anchor="middle">PACKAGING</text>
    <text class="use-label" x="1098" y="1267" text-anchor="middle">LABEL</text>
    <text class="use-label" x="1477" y="1267" text-anchor="middle">FOLDER COVER</text>
    <text class="use-label" x="1110" y="1582" text-anchor="middle">HANDICRAFT PAPER</text>
    <text class="use-label" x="1477" y="1582" text-anchor="middle">BUSINESS CARD</text>
  </g>
</svg>
</body>
</html>
```